Update of Personal Website: geraldmorton.net

This is a revamp of a personal website that already exists. Please visit the URL in the project title to view the current site.

An entirely fresh look is needed for the new site. Edits need to be made to the text included on the current site and photos must be added and subtracted. I will provide this.

Once a designer is selected, details about the necessities of the project will be discussed.

Target Market(s)

Business professionals

Industry/Entity Type

Real Estate Development

Coding

Coded - Design and coding required

Number of Pages Required

5+ page

Font styles to use
Sans Serif

Colors

Designer to choose colors to be used in the design.

Requirements
Must have
• Clean home page. Light background. Simplistic nature.
• Pages: Home, Family, Community, Business
Nice to have
• See attached images for examples of attractive sites.

```html
<!DOCTYPE html>
<html lang="en">
<head>
<meta charset="utf-8">
<title>Gerald Morton</title>
<link href="https://fonts.googleapis.com/css2?family=Montserrat:wght@600;700;800&family=Open+Sans:wght@400;600&display=swap" rel="stylesheet">
<style>
:root{
  --bg:#f4f5f7;
  --surface:#ffffff;
  --edge:#e1e3e8;
  --ink:#1b1c1f;
  --muted:#3b3d44;
  --accent:#1a44b8;
  --rule:#d4d7dd;
  --on-accent:#ffffff;
}
*{margin:0;padding:0;box-sizing:border-box}
html,body{width:1200px;height:1166px;overflow:hidden;background:var(--bg);color:var(--ink)}
body{position:relative;font-family:"Open Sans",sans-serif}

.site-header{position:absolute;left:0;top:0;width:1200px;height:77px;border-bottom:1px solid var(--rule);background:var(--surface)}
.brand{position:absolute;left:105px;top:25px;font:700 24px/28px "Montserrat",sans-serif;color:var(--ink);letter-spacing:.3px}
.main-nav{position:absolute;top:26px;right:96px;display:flex;gap:40px}
.main-nav a{font:600 14.5px/18px "Montserrat",sans-serif;color:var(--ink);text-decoration:none;padding-bottom:7px;letter-spacing:.3px}
.main-nav a.current{border-bottom:2px solid var(--accent);color:var(--accent)}

.hero{position:absolute;left:0;top:77px;width:1200px;height:503px;border-bottom:1px solid var(--rule)}
.hero-title{position:absolute;left:104px;top:95px;font:800 46px/56px "Montserrat",sans-serif;color:var(--ink);letter-spacing:-.5px}
.hero-title span{color:var(--accent)}
.hero-intro{position:absolute;left:104px;top:190px;width:607px;font-size:12.6px;line-height:23px;text-align:justify;color:var(--muted)}
.btn{position:absolute;left:104px;top:330px;width:125px;height:50px;background:var(--accent);color:var(--on-accent);border-radius:4px;font:600 17px "Open Sans",sans-serif;display:flex;align-items:center;justify-content:center;text-decoration:none}
.portrait{position:absolute;left:780px;top:26px;width:420px;height:476px;background:linear-gradient(160deg,#d9dbe0 0%,#b9bcc4 55%,#c98a55 100%);border-radius:4px 0 0 0}

.features{position:absolute;left:105px;top:668px;display:flex;gap:35px}
.card{width:309px;height:302px;background:var(--surface);border:3px solid var(--edge);text-align:center}
.card-media{height:198px}
.media-family{background:linear-gradient(135deg,#7d8550,#b39a66 60%,#5a5560)}
.media-community{background:linear-gradient(160deg,#2a4d9c,#5a86c8 55%,#8f7a80)}
.media-business{background:linear-gradient(180deg,#3a60cc,#c9a04c 60%,#6a553e)}
.card-title{margin-top:23px;font:700 18px/22px "Montserrat",sans-serif;color:var(--accent);letter-spacing:.3px}
.card-text{margin-top:11px;font-size:14.5px;line-height:20px;color:var(--muted)}

.site-footer{position:absolute;left:0;top:1058px;width:1200px;height:108px;border-top:2px solid var(--rule);background:var(--surface)}
.copyright{position:absolute;left:103px;top:44px;font-size:13px;line-height:18px;color:var(--muted)}
.social{position:absolute;left:1063px;top:33px;width:40px;height:40px;border-radius:50%;background:var(--accent);color:var(--on-accent);font:600 10px "Open Sans",sans-serif;display:flex;align-items:center;justify-content:center}
</style>
</head>
<body>
<header class="site-header">
  <div class="brand">GERALD MORTON</div>
  <nav class="main-nav">
    <a class="current" href="#">HOME</a>
    <a href="#">FAMILY</a>
    <a href="#">COMMUNITY</a>
    <a href="#">BUSINESS</a>
    <a href="#">BLOG</a>
    <a href="#">CONTACT</a>
  </nav>
</header>

<section class="hero">
  <h1 class="hero-title">GERALD <span>MORTON</span></h1>
  <p class="hero-intro">Gerald Morton completed his first real estate transaction at the age of 19. He is now one of the most recognized contributors to the real estate industry in the Southern United States. Morton is the driving force behind the upscale residential and mixed-use communities of Morton Development &amp; Realty LLC (MDR) and his most recent venture with Morton-Halloway.</p>
  <a class="btn" href="#">Read More</a>
  <div class="portrait" role="img" aria-label="Portrait photo of Gerald Morton in a grey suit"></div>
</section>

<section class="features">
  <article class="card">
    <div class="card-media media-family" role="img" aria-label="Family photo at home"></div>
    <h2 class="card-title">FAMILY</h2>
    <p class="card-text">Devoted husband and father of five...</p>
  </article>
  <article class="card">
    <div class="card-media media-community" role="img" aria-label="Glass residential towers at dusk"></div>
    <h2 class="card-title">COMMUNITY</h2>
    <p class="card-text">Committed to the community...</p>
  </article>
  <article class="card">
    <div class="card-media media-business" role="img" aria-label="Multi-family residential building at dusk"></div>
    <h2 class="card-title">BUSINESS</h2>
    <p class="card-text">Leading the Multi-family Development...</p>
  </article>
</section>

<footer class="site-footer">
  <p class="copyright">© Copyright 2017 Gerald Morton. All Rights Reserved</p>
  <a class="social">Follow</a>
</footer>
</body>
</html>
```